Corvel Partners 3 Fold Brochure

Hi, we need a 3 Fold brochure designed for our life coaching & hypnotherapy business.

The purpose of the brochure is to display our 3 main services - Success Coaching, Weight Loss and Quit Smoking. We would like to see designs that are simple to read, and attractive. The colors used are not important, as long as they work well with our logo and overall theme.

The uploading and print specifications we need for printing can be found here:

http://www.plenmark-example.com.au/custom-brochures.aspx?txi=27316&xnid=TopNav_Brochures+(linked+item)_Marketing+Materials_All+Products&xnav=TopNav

Please find our logo files and content we require for the brochure (word doc) attached.

Thank You!

Industry/Entity Type

Life Coaching

Requirements
Must have
• Must have logo somewhere on front page
Nice to have
• Images relevant for each of the 3 services
Highlight the Special Offer on the back in some way

```html
<!DOCTYPE html>
<html lang="en">
<head>
<meta charset="utf-8">
<title>Corvel Partners – Tri-fold Brochure Inside</title>
<link href="https://fonts.googleapis.com/css2?family=Arimo:ital,wght@0,400;0,700;1,400;1,700&display=swap" rel="stylesheet">
<style>
:root{
  --band:#4d87e3;
  --heading:#1f5ea8;
  --accent:#1c63b8;
  --ink:#111;
  --paper:#fff;
  --photo-coach:#c9c2bb;
  --photo-waist:#b48a6e;
  --photo-smoke:#6a5a52;
}
*{box-sizing:border-box;margin:0;padding:0}
html,body{width:1200px;height:931px;overflow:hidden;background:var(--paper)}
body{font-family:"Arimo",Arial,sans-serif;color:var(--ink);position:relative}
.band{position:absolute;left:0;width:1200px;background:var(--band);z-index:0}
.band-top{top:0;height:24px}
.band-mid{top:223px;height:9px}
.band-bottom{top:902px;height:29px}
.photo{position:absolute;top:26px;height:197px}
.photo-coach{left:12px;width:381px;background:linear-gradient(160deg,#f3f1ee 0%,var(--photo-coach) 60%,#3b3431 100%)}
.photo-waist{left:401px;width:390px;background:radial-gradient(ellipse at 55% 50%,#d6ae8e 0%,var(--photo-waist) 55%,#3a2b22 100%)}
.photo-smoke{left:800px;width:386px;background:radial-gradient(ellipse at 50% 55%,#e2c3b0 0%,var(--photo-smoke) 50%,#151212 100%)}
.panel{position:absolute;top:0;height:931px;z-index:1}
.panel-coaching{left:20px;width:362px}
.panel-weight{left:408px;width:396px}
.panel-smoking{left:800px;width:392px}
.blk{position:absolute;left:0;right:0;white-space:nowrap}
.center{text-align:center}
h2{font-size:19px;line-height:24px;font-weight:700;color:var(--heading);text-align:center;letter-spacing:.3px}
.hl{color:var(--accent);font-weight:700}
.lead{font-size:16.5px;line-height:20.4px}
.body{font-size:16px;line-height:19.2px}
.pkg{font-size:15.5px;line-height:19.2px}
.pkg-title{font-weight:700}
.pkg-plan{font-style:italic}
.pkg-note{font-size:12px;font-style:italic;line-height:14.4px}
.cta{font-style:italic;font-size:16.5px;line-height:20.4px}
h3{font-size:16.5px;font-weight:700;line-height:19.6px;text-align:center}
h4{font-size:16.5px;font-weight:700;color:var(--heading);line-height:19.2px;text-align:center}
ul.bullets{list-style:none;font-size:16px}
ul.bullets li{position:relative;padding-left:14px}
ul.bullets li::before{content:"";position:absolute;left:0;top:6px;width:8px;height:8px;border-radius:50%;background:var(--ink)}
.price{font-size:17px;line-height:20px;text-align:center}
.strong{font-weight:700}
.q{font-size:15.5px;font-weight:700;line-height:19.2px}
.small-cta{font-size:13.5px;font-weight:700;line-height:18px;text-align:center}
</style>
</head>
<body>
<div class="band band-top"></div>
<div class="photo photo-coach" role="img" aria-label="Coach presenting to an enthusiastic audience"></div>
<div class="photo photo-waist" role="img" aria-label="Measuring tape around a slim waist"></div>
<div class="photo photo-smoke" role="img" aria-label="Hands snapping a cigarette in half"></div>
<div class="band band-mid"></div>

<section class="panel panel-coaching">
  <h2 class="blk" style="top:241px">PERSONAL SUCCESS COACHING</h2>
  <p class="blk lead center" style="top:272px"><span class="hl">IMAGINE</span> having your own<br>Personal Success Coach working with<br>you to help you achieve your dreams.<br>Whether you're feeling frustrated in your<br>present career, searching for new<br>opportunities, or simply wishing to get<br>more out of life, we can help <span class="hl">YOU</span> to<br>close the gap between where you are<br>and where you <span class="hl">WANT</span> to be.</p>
  <div class="blk pkg" style="top:464px">
    <p class="pkg-title">1 Session&nbsp; Hour of Power</p>
    <p>Investment - $150</p>
    <p class="pkg-note">A 60 minute breakthrough session where we focuson a<br>particular problem at hand that you want to solve right <b>NOW.</b></p>
  </div>
  <div class="blk pkg" style="top:536px">
    <p class="pkg-title">3 Sessions&nbsp; Unlock Your Potential</p>
    <p>Investment - $390 (Save $60)</p>
    <p class="pkg-plan">Payment Plan Available</p>
    <p class="pkg-note">This 3 step program is ideal for someone who wants to set<br>and attain their goals and build confidence.</p>
  </div>
  <div class="blk pkg" style="top:633px">
    <p class="pkg-title">5 Sessions&nbsp; Unleash Your Potential</p>
    <p>Investment - $625 (Save $125)</p>
    <p class="pkg-plan">Payment Plan Available</p>
    <p class="pkg-note">This 5 step program is ideal for someone who wants to let<br>go of their limitations and create the life they want.</p>
  </div>
  <div class="blk pkg" style="top:721px">
    <p class="pkg-title">BEST VALUE!!</p>
    <p class="pkg-title">10 Sessions&nbsp; Beyond Your Potential</p>
    <p>Investment - $1000 (Save $500)</p>
    <p class="pkg-plan">Payment Plan Available</p>
    <p class="pkg-note">An in depth program ideal for someone who wants to go<br>beyond their potential and turn their dreams into an actual<br>reality.</p>
  </div>
  <p class="blk cta center" style="top:841px">Not sure which plan to choose?<br>Call <b>NOW</b> to discuss which plan will best serve<br>your needs and ultimately lead to your success!</p>
</section>

<section class="panel panel-weight">
  <h2 class="blk" style="top:241px">WEIGHT LOSS</h2>
  <p class="blk body center" style="top:275px;font-size:16.5px">When you close your eyes, it's easy to<br>imagine your ideal figure. Go one step further<br>and put your unconscious to work on your<br>weight loss goals with our<br><span class="hl">Weight Loss Hypnosis &amp; Coaching Session.</span></p>
  <h3 class="blk" style="top:380px">Want To Achieve Fast Fat Loss And<br>Increase Growth Hormone?</h3>
  <p class="blk body center" style="top:430px;line-height:18.6px">With our Weight Loss Hypnosis &amp; Coaching<br>Program you can finally get rid of that ugly<br>body fat and even build lean muscle, all while<br>maintaining a healthy metabolism.<br>Some benefits of our program...</p>
  <ul class="blk bullets" style="top:533px;line-height:19.4px;left:6px">
    <li>You won't have to avoid going to restaurants<br>with your friends</li>
    <li>You will stop thinking of food and eating all<br>the time</li>
    <li>You can still enjoy regular food</li>
    <li>You will have more energy and boost fat<br>burning hormones</li>
    <li>You will save money</li>
  </ul>
  <h4 class="blk" style="top:690px">Dieting Doesn't Work!</h4>
  <p class="blk body center" style="top:710px">Once you experience how easy it is to eat<br>right, exercise and lose weight, you will wish<br>you had discovered this program sooner!</p>
  <h4 class="blk" style="top:770px">The Solution</h4>
  <p class="blk body center" style="top:790px;line-height:19px">Discover our simple secret eating strategy.<br>Our proven system will help you to<br>systematically adopt healthy eating and<br>exercise habits for the rest of your life.</p>
  <p class="blk body center strong" style="top:862px">Call <span class="hl">NOW</span> and get started today!</p>
  <p class="blk price" style="top:881px">Investment - $150</p>
</section>

<section class="panel panel-smoking">
  <h2 class="blk" style="top:241px">QUIT SMOKING</h2>
  <p class="blk body center" style="top:272px;font-size:16.5px;line-height:19.8px">We can help YOU become a <span class="hl">non smoker</span> using<br>the most advanced methods of NLP and<br>Hypnosis.</p>
  <h3 class="blk" style="top:339px;line-height:20.4px">Imagine The Rest Of Your Life No<br>Longer Craving Cigarettes!</h3>
  <ul class="blk bullets" style="top:383px;line-height:18.5px;left:12px">
    <li>Our system will help you to overcome all the<br>reasons why you smoke so that you don't feel<br>like you're giving anything up, you just<br><span class="hl">CHOOSE</span> to do something more healthy and<br>resourceful.</li>
    <li>Our system deals with the mental, emotional<br>and physical reasons which have prevented you<br>from successfully quitting in the past.</li>
  </ul>
  <p class="blk q" style="top:543px;left:12px">How Much Are Cigarettes Really Costing You?</p>
  <p class="blk body center" style="top:566px">What is the real cost for maintaining this habit...<br>Coughing and wheezing, bad breath, low<br>energy levels, poor sex life, worrying yourself<br>sick about your health?</p>
  <h4 class="blk" style="top:650px">What is Hypnosis?</h4>
  <p class="blk body center" style="top:670px;line-height:18.3px">Our minds work on two levels... the Conscious<br>Mind and the Unconscious Mind. We think, act and<br>make decisions with our conscious mind.<br>However, 96% of our mind in unconscious, and it<br>is our unconscious mind that controls our habits.<br>In the relaxed state known as hypnosis, our critical<br>faculty is bypassed, meaning we can communicate<br>directly with the unconscious mind. This is why we<br>can change a lifelong habit quickly and easily<br>using hypnosis.</p>
  <p class="blk small-cta" style="top:858px">Ready to get started? Call <span class="hl">NOW</span> and change your life!</p>
  <p class="blk price" style="top:879px">Investment - $200</p>
</section>

<div class="band band-bottom"></div>
</body>
</html>
```